Business Process / Lifecycle Diagram for Consulting Firm

We are a Delaware-based business modernization and transition-readiness firm. We need a clean, professional process diagram that visually represents our client lifecycle. This is not a marketing funnel or sales graphic — it is a product and delivery lifecycle.

The diagram must be reusable across pitch decks, one-pagers, grant applications, and our website.

Required Structure (must follow exactly)
Stage 1 — Diagnose
Enterprise Upgrade Audit (EUA)
Shift Preparedness Gauge™ (SPG)
(Parallel entry points, equal visual weight)

→ Output: Diagnostic Insight & Priority Signals

Stage 2 — Clarify
Modernization Roadmap (Co-Created)

Stage 3 — Modernize
Q7 — Margin & Momentum Track

Stage 4 — Sustain
Ongoing Modernization Support

Foundation Layer (supports all stages)
HRG-OS™ pillars: People, Process, Systems, Insight

End Outcome
- Operational Clarity
- Sustainable Profitability
- Long-Term Stability

Design Requirements
- Professional, calm (not startup / SaaS style)
- Minimal text, clear hierarchy
- Horizontal or left-to-right flow preferred
- No funnels, no sales language, no aggressive arrows
- Must be delivered as editable vector (AI, SVG, or Figma)

Brand Notes
- Neutral color palette that complements logo attached (Gold Color Code C39E11, Navy Blue code 002C55)
- One accent color for emphasis
- Clean typography
- Should feel credible to business owners, advisors, and lenders
- See website (https://www.hazelmereridgegroup.com/) and LinkedIn (https://www.hazelmereridgegroup.com/) for additional insight into branding.

What NOT to Do
- Do not rename stages
- Do not combine stages
- Do not add extra steps

```html
<!DOCTYPE html>
<html lang="en">
<head>
<meta charset="utf-8">
<title>Hazelmere Ridge Group — Client Lifecycle</title>
<link href="https://fonts.googleapis.com/css2?family=Open+Sans:wght@400;600;700&display=swap" rel="stylesheet">
<style>
  :root {
    --navy: #0b2d83;
    --gold: #bf9a0a;
    --mist: #edf4f2;
    --band: #e3efec;
    --arrow: #7b9ea6;
    --white: #ffffff;
  }
  * { box-sizing: border-box; margin: 0; padding: 0; }
  html, body { width: 1200px; height: 586px; overflow: hidden; background: var(--white); }
  body { position: relative; font-family: "Open Sans", Arial, sans-serif; color: var(--navy); }
  .abs { position: absolute; }

  .brand { left: 0; width: 1200px; top: 78px; display: flex; justify-content: center; align-items: center; gap: 10px; }
  .brand-mark { width: 14px; height: 14px; background: var(--gold); }
  .brand-name { font-size: 26px; font-weight: 600; letter-spacing: 3px; color: var(--navy); text-transform: uppercase; }

  .stage-label { top: 185px; width: 200px; text-align: center; color: var(--gold); font-size: 17px; font-weight: 600; }

  .stage-band { left: 57px; top: 220px; }
  .stage-name { top: 220px; height: 32px; line-height: 32px; text-align: center; color: var(--white); font-size: 16.5px; font-weight: 700; letter-spacing: .3px; }

  .box { display: flex; align-items: center; justify-content: center; text-align: center; border: 1px solid var(--navy); background: var(--mist); font-size: 14px; line-height: 1.2; }
  .box.small { font-size: 13.3px; line-height: 1.05; }
  .box.accent { background: var(--gold); border-color: var(--gold); color: var(--white); }
  .box.output { background: var(--navy); color: var(--white); font-size: 11px; font-weight: 700; border: none; }

  .down { left: 151px; top: 325px; }
  .flow-arrow { top: 307px; }

  .outcome { left: 983px; top: 276px; width: 173px; height: 127px; background: var(--navy); color: var(--white); padding: 16px 0 0 10px; }
  .outcome h2 { font-size: 17.5px; font-weight: 700; margin: 0 0 10px 7px; }
  .outcome li { list-style: none; font-size: 13px; line-height: 20.7px; display: flex; align-items: center; }
  .outcome li::before { content: ""; width: 5px; height: 5px; border-radius: 50%; background: var(--gold); margin-right: 2px; }

  .pillars-head { left: 57px; top: 409px; width: 910px; height: 35px; background: var(--navy); border-radius: 9px 9px 0 0; color: var(--white); text-align: center; font-size: 21px; line-height: 35px; }
  .pillars-head sup { font-size: 11px; }
  .pillars { left: 57px; top: 444px; width: 910px; height: 49px; background: var(--band); display: flex; }
  .pillar { flex: 1; display: flex; align-items: center; justify-content: center; gap: 5px; font-size: 19px; position: relative; }
  .pillar + .pillar::before { content: ""; position: absolute; left: 0; top: 12px; height: 28px; border-left: 1.5px solid var(--navy); }
</style>
</head>
<body>

<header class="abs brand">
  <span class="brand-mark"></span>
  <span class="brand-name">Hazelmere Ridge Group</span>
</header>

<div class="abs stage-label" style="left:61px">Stage 1</div>
<div class="abs stage-label" style="left:291px">Stage 2</div>
<div class="abs stage-label" style="left:524px">Stage 3</div>
<div class="abs stage-label" style="left:755px">Stage 4</div>

<svg class="abs stage-band" width="903" height="32" viewBox="0 0 903 32">
  <polygon points="0,0 225,0 238,16 225,32 0,32" fill="#0b2d83"/>
  <polygon points="227,0 451,0 464,16 451,32 227,32 240,16" fill="#0b2d83"/>
  <polygon points="453,0 677,0 690,16 677,32 453,32 466,16" fill="#bf9a0a"/>
  <path d="M679,0 H898 Q902,0 902,4 V32 H679 L692,16 Z" fill="#0b2d83"/>
</svg>
<div class="abs stage-name" style="left:57px;width:210px">DIAGNOSE</div>
<div class="abs stage-name" style="left:291px;width:207px">CLARIFY</div>
<div class="abs stage-name" style="left:521px;width:207px">MODERNIZE</div>
<div class="abs stage-name" style="left:752px;width:207px">SUSTAIN</div>

<div class="abs box small" style="left:57px;top:262px;width:104px;height:57px">Enterprise<br>Upgrade<br>Audit (EUA)</div>
<div class="abs box small" style="left:163px;top:262px;width:104px;height:57px">Shift<br>Preparedness<br>Gauge™ (SPG)</div>
<svg class="abs down" width="22" height="10" viewBox="0 0 22 10"><polygon points="0,0 22,0 11,10" fill="#7b9ea6"/></svg>
<div class="abs box output" style="left:57px;top:342px;width:210px;height:29px">Diagnostic Insight &amp; Priority Signals</div>

<div class="abs box" style="left:291px;top:276px;width:207px;height:78px">Modernization Roadmap<br>(Co-Created)</div>
<div class="abs box accent" style="left:521px;top:276px;width:207px;height:78px">Q7 — Margin<br>&amp; Momentum Track</div>
<div class="abs box" style="left:752px;top:276px;width:207px;height:78px">Ongoing<br>Modernization Support</div>

<svg class="abs flow-arrow" style="left:269px" width="18" height="16" viewBox="0 0 18 16"><path d="M0,5 H9 V0 L18,8 L9,16 V11 H0 Z" fill="#7b9ea6"/></svg>
<svg class="abs flow-arrow" style="left:501px" width="18" height="16" viewBox="0 0 18 16"><path d="M0,5 H9 V0 L18,8 L9,16 V11 H0 Z" fill="#7b9ea6"/></svg>
<svg class="abs flow-arrow" style="left:731px" width="18" height="16" viewBox="0 0 18 16"><path d="M0,5 H9 V0 L18,8 L9,16 V11 H0 Z" fill="#7b9ea6"/></svg>
<svg class="abs flow-arrow" style="left:963px" width="18" height="16" viewBox="0 0 18 16"><path d="M0,5 H9 V0 L18,8 L9,16 V11 H0 Z" fill="#7b9ea6"/></svg>

<section class="abs outcome">
  <h2>End Outcome</h2>
  <ul>
    <li>Operational Clarity</li>
    <li>Sustainable Profitability</li>
    <li>Long-Term Stability</li>
  </ul>
</section>

<div class="abs pillars-head">HRG-OS<sup>™</sup> pillars</div>
<div class="abs pillars">
  <div class="pillar">
    <svg width="24" height="24" viewBox="0 0 24 24" fill="none" stroke-width="1.4">
      <circle cx="9" cy="5" r="3" stroke="#bf9a0a"/>
      <circle cx="5" cy="13" r="2.6" stroke="#0b2d83"/><circle cx="17" cy="13" r="2.6" stroke="#0b2d83"/>
      <path d="M1 23c0-4 2-6 4-6s4 2 4 6M13 23c0-4 2-6 4-6s4 2 4 6" stroke="#0b2d83"/>
    </svg>People
  </div>
  <div class="pillar">
    <svg width="22" height="24" viewBox="0 0 22 24" fill="none" stroke="#0b2d83" stroke-width="1.4">
      <rect x="1" y="1" width="20" height="22"/><path d="M1 18h20M4 6h14M4 12h14"/>
      <circle cx="8" cy="6" r="1.5" fill="#bf9a0a" stroke="none"/><circle cx="14" cy="12" r="1.5" fill="#bf9a0a" stroke="none"/>
    </svg>Process
  </div>
  <div class="pillar">
    <svg width="28" height="24" viewBox="0 0 28 24" fill="none" stroke-width="1.5">
      <circle cx="8" cy="8" r="4" stroke="#0b2d83" stroke-dasharray="2 1.5"/>
      <circle cx="18" cy="15" r="5.5" stroke="#bf9a0a" stroke-dasharray="2.4 1.6"/>
      <circle cx="18" cy="15" r="2" stroke="#bf9a0a"/>
    </svg>Systems
  </div>
  <div class="pillar">
    <svg width="22" height="22" viewBox="0 0 22 22" fill="none" stroke-width="1.6">
      <path d="M1 2v19h20" stroke="#0b2d83"/>
      <path d="M5 16l10-10M11 5h5v5" stroke="#bf9a0a"/>
    </svg>Insight
  </div>
</div>

</body>
</html>
```